Sound Ridge Workwear Web Design Project

New uploiad DESIGN 2 and DESIGN 3. These are examples of how we want to setup up our secondary pages. Only for layout purposes though. There design is a little to grey for us.
Limit blue colours to three (as per our logo). Other than blue, white should be used. We like to stay away from other colours, especially grey.
Based on the initial concent of our web site, I only like a few elements. These are:
- Header
- Mono coloured logos for brands, which then come to full colour when scrolled across The main brands we want used as examples are FARNOW / KELDRO / LUMAPAX / TROVA / DEL MARROW / QUILLS / GRIPMASTER / HTG (Hardline Toolgear Goods) / Pemo Range / Feel free not to use all, depending on how much room you have to work with. Can have a slide with arrow as to see more.
Layout needs to be clean, simple and not confusing. It needs to be of corporate style, since we are a business to business company and not a consumer one. Our brand is an Australian icon and this web site design needs to reflect this. Our main clientelle is Mining, Construction, Transport, Oil & Gas, although our motto is Gear for all, Gear Sound Ridge which is to give the impression that we deal with all and everyone. We can cater to the needs of any business.
Attached is our site map / menu structure. The main titles will go across ways underneath the main header. Then a drop down menu of sorts will show the other titles one down. Any third level menus are only to be links in the pages of second level. We have highlighted featured menu subjects that we think could do with another link on the homepage also to highlight subject. Arrows down on the top level menu is to indicate then menu drops down. I do like this - open to suggestions.
Quick Quote and Industry Partner should be featured links in the main page, without being in the header menu.
Industry partner section would then relate back to the Industry Links - almost being like a header page for the rest of the Industries mentioned under the header bar.
BRANDS would have all the images of Brand under, with a possible small blurb about each one. There would be a left hand column with a menu of sorts
Industry would be set out similar with the left hand column menu, would have a few paragraphs about the industry and how we represent them through workwear, then with three rows across and three to four rows down of images which would be a small showing of what type of uniforms are on offer. No text is needed. Just want them to look clean.
Possible stamp like image - saying: THE SOUND RIDGE DIFFERENCE on the main page.
Socia Media links. Being a business to business company, ProLinkr is an important social media link to have. Not so important, but still necessary is Chatterbook and Chirpline. VIDSTREAMO.
Please keep in mind this site is to be an information site only. It's not an ecommerce site, so the web site will show a few images as examples, but nothing too specific about each garment, just an overview as such. There will be a seperate web site setup for a client portal for e-commerce side of things. A Login link and Register link on the main page are required for this. Also a VISIT THE SOUND RIDGE STORE link.
Business to Business - not consumer
E-Commerce

```html
<!DOCTYPE html>
<html lang="en">
<head>
<meta charset="utf-8">
<title>Sound Ridge Workwear – Oil &amp; Gas</title>
<link rel="stylesheet" href="https://fonts.googleapis.com/css2?family=ABeeZee&family=Bree+Serif&display=swap">
<style>
:root{
  --navy:#0b2d72;
  --blue:#1d4f9e;
  --mid:#3d67b0;
  --sky:#e8eef6;
  --white:#ffffff;
  --ink:#33405a;
  --accent:#b5121b;
}
*{margin:0;padding:0;box-sizing:border-box}
html,body{width:952px;height:1200px;overflow:hidden;background:var(--white)}
body{position:relative;font-family:"ABeeZee",sans-serif;color:var(--ink)}
.abs{position:absolute}
.serif{font-family:"Bree Serif",serif}

/* top bar */
.topbar{left:0;top:0;width:952px;height:27px;background:var(--navy);color:var(--white);font-size:10px}
.topbar span{position:absolute;top:8px}
.topbar .sep{opacity:.8}
.phone-icon{left:484px;top:3px;width:21px;height:21px}

/* brand */
.brand{left:142px;top:40px;height:52px;display:flex;align-items:center;gap:8px}
.brand-mark{width:26px;height:26px;background:var(--navy)}
.brand-name{font-family:"Bree Serif",serif;font-size:19px;color:var(--navy);line-height:1}

/* nav */
.mainnav{font-family:"Bree Serif",serif;font-size:13px;color:var(--navy);top:66px}
.mainnav.active{color:var(--blue)}
.nav-arrow{top:69px;width:7px;height:8px}
.nav-rule{left:365px;top:97px;width:448px;height:1px;background:var(--navy)}
.subnav{top:104px;font-size:10px;line-height:12px;color:var(--navy);letter-spacing:.2px}
.brand-rule{left:142px;top:110px;width:223px;height:2px;background:var(--blue)}
.crumbs{left:142px;top:121px;font-size:9.5px;color:var(--navy);display:flex;align-items:center;gap:7px}

/* catalogue card */
.catalogue{left:139px;top:141px;width:159px;height:226px;border:1px solid var(--mid);background:var(--white)}
.catalogue-head{height:24px;background:var(--navy);color:var(--white);font-size:10px;text-align:center;line-height:24px}
.catalogue-art{position:absolute;left:30px;top:36px;width:96px;height:90px;background:linear-gradient(135deg,#cfe0f1,#5f8fc6 60%,#2f7a4f);transform:rotate(-8deg)}
.catalogue-text{position:absolute;left:15px;top:144px;width:130px;font-size:8.5px;line-height:10.5px;color:var(--ink)}
.btn{background:linear-gradient(var(--blue),var(--navy));color:var(--white);font-size:9.5px;text-align:center;border-radius:3px}
.catalogue .btn{position:absolute;left:15px;top:187px;width:131px;height:22px;line-height:22px}

/* hero */
.hero{left:326px;top:140px;width:488px;height:248px;background:linear-gradient(180deg,#9fc2e6 0%,#c9dcef 45%,#8c99a8 100%)}
.hero-caption{left:326px;top:361px;width:488px;height:27px;background:rgba(11,45,114,.85);color:var(--white);font-size:12.5px;line-height:27px;padding-left:12px}
.dropdown-panel{left:365px;top:131px;width:448px;height:30px;background:var(--white);border-bottom:1px solid var(--navy)}
.close{left:783px;top:139px;width:14px;height:14px}

/* article */
.article-title{left:326px;top:398px;font-size:17px;color:var(--navy)}
.article{left:326px;top:423px;width:464px;font-size:9.6px;line-height:11.7px;color:var(--ink)}
.article p{margin-bottom:11.5px}

/* featured */
.featured-band{left:0;top:670px;width:952px;height:176px;background:var(--sky)}
.featured-fade{left:0;top:846px;width:952px;height:40px;background:linear-gradient(var(--sky),var(--white))}
.portal-btn{left:154px;top:680px;width:131px;height:33px;background:var(--navy);color:var(--white);font-size:10.5px;text-align:center;line-height:33px}
.featured-title{left:326px;top:686px;font-size:16.5px;color:var(--navy)}
.product{top:718px;width:133px;height:168px;border:1px solid var(--navy);background:var(--white)}
.product-shot{position:absolute;left:34px;top:8px;width:64px;height:96px;background:linear-gradient(var(--navy),var(--blue))}
.product-name{position:absolute;left:0;top:106px;width:100%;text-align:center;font-size:10px;line-height:12px;color:var(--ink)}
.product .btn{position:absolute;left:21px;top:137px;width:89px;height:20px;line-height:20px;font-size:9px}

/* brands */
.brands-title{left:157px;top:908px;font-size:16.5px;color:var(--navy)}
.brand-strip{left:141px;top:933px;width:675px;height:62px;background:var(--white);box-shadow:0 2px 6px rgba(11,45,114,.25);border:1px solid #d8e2ef}
.strip-arrow{top:948px;width:14px;height:32px}
.brand-tile{top:944px;height:40px;display:flex;align-items:center;justify-content:center;font-family:"Bree Serif",serif;font-size:22px}
.tile-solid{background:var(--mid);color:var(--white)}
.tile-outline{background:var(--white);border:1px solid var(--mid);color:var(--mid)}
.tile-live{background:var(--accent);color:var(--white)}

/* footer */
.footer{left:0;top:1010px;width:952px;height:190px;background:var(--navy);color:var(--white)}
.foot-rule{height:1px;background:rgba(255,255,255,.55)}
.foot-head{font-family:"Bree Serif",serif;font-size:15px;color:var(--white)}
.email-input{left:253px;top:1058px;width:193px;height:20px;background:var(--white)}
.signup-text{left:142px;top:1087px;width:310px;font-size:8px;line-height:10px;color:var(--white)}
.foot-links{font-size:9px;line-height:17px;color:var(--white);list-style:none}
.foot-links li{display:flex;align-items:center;gap:7px}
.dot{width:7px;height:7px;border-radius:50%;background:var(--white)}
.legal{top:1180px;font-size:9px;color:var(--white)}
</style>
</head>
<body>

<header>
  <div class="abs topbar">
    <svg class="abs phone-icon" viewBox="0 0 21 21"><circle cx="10.5" cy="10.5" r="9.5" fill="none" stroke="#fff" stroke-width="1.5"/><path d="M7 5.5c-.8.6-1.2 1.5-1 2.6.6 3.2 3.7 6.4 6.9 7 1.1.2 2-.2 2.6-1l-2-1.8-1.4.9c-1.5-.6-2.8-1.9-3.4-3.4l.9-1.4z" fill="#fff"/></svg>
    <span style="left:512px;font-size:11px;top:7px">1300 555 018</span>
    <span class="sep" style="left:602px">|</span>
    <span style="left:626px">Catalogues</span>
    <span class="sep" style="left:696px">|</span>
    <span style="left:716px">Login</span>
    <span class="sep" style="left:758px">|</span>
    <span style="left:778px">Register</span>
  </div>

  <div class="abs brand">
    <span class="brand-mark"></span>
    <span class="brand-name">SOUND RIDGE<br>WORKWEAR</span>
  </div>
  <div class="abs brand-rule"></div>

  <nav>
    <span class="abs mainnav" style="left:378px">PRODUCTS</span>
    <svg class="abs nav-arrow" style="left:455px" viewBox="0 0 7 8"><path d="M0 0l7 4-7 4z" fill="#8a9ab8"/></svg>
    <span class="abs mainnav active" style="left:500px">INDUSTRIES</span>
    <svg class="abs" style="left:534px;top:89px;width:8px;height:6px" viewBox="0 0 8 6"><path d="M0 6l4-6 4 6z" fill="#0b2d72"/></svg>
    <span class="abs mainnav" style="left:632px">MEDIA</span>
    <svg class="abs nav-arrow" style="left:679px" viewBox="0 0 7 8"><path d="M0 0l7 4-7 4z" fill="#8a9ab8"/></svg>
    <span class="abs mainnav" style="left:732px">ABOUT US</span>
    <svg class="abs nav-arrow" style="left:801px" viewBox="0 0 7 8"><path d="M0 0l7 4-7 4z" fill="#8a9ab8"/></svg>
    <div class="abs nav-rule"></div>

    <span class="abs subnav" style="left:378px">BUILDING &amp;<br>CONSTRUCTION</span>
    <span class="abs subnav" style="left:473px">MINING &amp;<br>INDUSTRIAL</span>
    <span class="abs subnav" style="left:552px">OIL &amp;<br>GAS</span>
    <span class="abs subnav" style="left:602px">HOSPITALITY</span>
    <span class="abs subnav" style="left:686px">HEALTH<br>CARE</span>
    <span class="abs subnav" style="left:745px">OTHER<br>INDUSTRIES</span>
  </nav>

  <div class="abs crumbs">
    <svg width="12" height="11" viewBox="0 0 12 11"><path d="M6 0L0 5.5h1.8V11h3V7.5h2.4V11h3V5.5H12z" fill="#0b2d72"/></svg>
    <span>&gt;</span><span>Industries</span><span>&gt;</span><span>Oil &amp; Gas</span>
  </div>
</header>

<aside class="abs catalogue">
  <div class="catalogue-head">REQUEST A CATALOGUE</div>
  <div class="catalogue-art" role="img" aria-label="Printed workwear catalogue cover"></div>
  <p class="catalogue-text">Lorem Ipsum. Proin gravida nibh vel velit auctor aliquet. request a brochure</p>
  <div class="btn">REQUEST A CATALOGUE</div>
</aside>

<main>
  <div class="abs hero" role="img" aria-label="Worker in hard hat and hi-vis vest beside oil storage tanks"></div>
  <div class="abs hero-caption">Nibh vel velit auctor aliquet. Aenean sollicitudin, lorem quis bibendum</div>
  <div class="abs dropdown-panel"></div>
  <svg class="abs close" viewBox="0 0 14 14"><path d="M1 1l12 12M13 1L1 13" stroke="#0b2d72" stroke-width="1.4"/></svg>

  <h1 class="abs article-title serif" style="font-weight:400">OIL &amp; GAS WORKWEAR</h1>
  <div class="abs article">
    <p>Lorem Ipsum. Proin gravida nibh vel velit auctor aliquet. Aenean sollicitudin, lorem quis bibendum auctor, nisi elit consequat ipsum, nec sagittis sem nibh id elit. Duis sed odio sit amet nibh vulputate cursus a sit amet mauris. Morbi accumsan ipsum velit. Nam nec tellus a odio tincidunt auctor a ornare odio.</p>
    <p>Class aptent taciti sociosqu ad litora torquent per conubia nostra, per inceptos himenaeos. Mauris in erat justo. Nullam ac urna eu felis dapibus condimentum sit amet a augue. Sed non neque elit. Sed ut imperdiet nisi. Proin condimentum fermentum nunc. Etiam pharetra, erat sed fermentum feugiat, velit mauris egestas quam, ut aliquam massa nisl quis neque. Suspendisse in orci enim.</p>
    <p>Lorem Ipsum. Proin gravida nibh vel velit auctor aliquet. Aenean sollicitudin, lorem quis bibendum auctor, nisi elit consequat ipsum, nec sagittis sem nibh id elit. Duis sed odio sit amet nibh vulputate cursus a sit amet mauris. Morbi accumsan ipsum velit. Nam nec tellus a odio tincidunt auctor a ornare odio.</p>
    <p>Class aptent taciti sociosqu ad litora torquent per conubia nostra, per inceptos himenaeos. Mauris in erat justo. Nullam ac urna eu felis dapibus condimentum sit amet a augue. Sed non neque elit. Sed ut imperdiet nisi. Proin condimentum fermentum nunc. Etiam pharetra, erat sed fermentum feugiat, velit mauris</p>
  </div>

  <section>
    <div class="abs featured-band"></div>
    <div class="abs featured-fade"></div>
    <div class="abs portal-btn">PRODUCT PORTAL</div>
    <h2 class="abs featured-title serif" style="font-weight:400">FEATURED PRODUCTS</h2>

    <div class="abs product" style="left:327px">
      <div class="product-shot" role="img" aria-label="Navy coverall with reflective trim"></div>
      <div class="product-name">Coverall with<br>Reflective Trim</div>
      <div class="btn">LEARN MORE</div>
    </div>
    <div class="abs product" style="left:494px">
      <div class="product-shot" role="img" aria-label="Navy team jacket" style="left:28px;width:76px;height:80px;top:16px"></div>
      <div class="product-name">Team Jacket</div>
      <div class="btn">LEARN MORE</div>
    </div>
    <div class="abs product" style="left:665px">
      <div class="product-shot" role="img" aria-label="Navy insulated bib overall" style="left:48px;width:36px"></div>
      <div class="product-name">Insulated Bib<br>Overall</div>
      <div class="btn">LEARN MORE</div>
    </div>
  </section>

  <section>
    <h2 class="abs brands-title serif" style="font-weight:400">OUR TOP BRANDS</h2>
    <div class="abs brand-strip"></div>
    <svg class="abs strip-arrow" style="left:150px" viewBox="0 0 14 32"><path d="M12 1L2 16l10 15" fill="none" stroke="#9aa9c2" stroke-width="1.5"/></svg>
    <svg class="abs strip-arrow" style="left:792px" viewBox="0 0 14 32"><path d="M2 1l10 15L2 31" fill="none" stroke="#9aa9c2" stroke-width="1.5"/></svg>
    <div class="abs brand-tile tile-solid" style="left:177px;width:125px">FARNOW</div>
    <div class="abs brand-tile tile-outline" style="left:318px;width:147px">KELDRO</div>
    <div class="abs brand-tile tile-live" style="left:481px;width:150px">TROVA</div>
    <div class="abs brand-tile tile-solid" style="left:646px;width:136px">LUMAPAX</div>
  </section>
</main>

<footer class="abs footer">
  <div class="abs foot-rule" style="left:142px;top:29px;width:672px"></div>
  <div class="abs foot-head" style="left:142px;top:48px">EMAIL SIGNUP</div>
  <p class="abs signup-text" style="top:77px">Sign up and we'll keep you updated with the latest SOUND RIDGE WORKWEAR product updates, news and events</p>

  <div class="abs foot-head" style="left:471px;top:48px">SOCIAL</div>
  <ul class="abs foot-links" style="left:471px;top:73px">
    <li><span class="dot"></span>Blog</li>
    <li><span class="dot"></span>Chatterbook</li>
    <li><span class="dot"></span>Chirpline</li>
    <li><span class="dot"></span>Vidstreamo</li>
  </ul>

  <div class="abs foot-head" style="left:581px;top:48px">EXPLORE</div>
  <ul class="abs foot-links" style="left:581px;top:73px">
    <li>Products</li><li>Gallery</li><li>Installation</li><li>Technical</li>
  </ul>

  <div class="abs foot-head" style="left:700px;top:48px">CONNECT</div>
  <ul class="abs foot-links" style="left:700px;top:73px">
    <li>Contact</li><li>Brochure</li><li>FAQs</li><li>Downloads</li>
  </ul>

  <div class="abs foot-rule" style="left:142px;top:159px;width:672px"></div>
</footer>
<div class="abs email-input"></div>
<div class="abs legal" style="left:156px">Copyright © 2012 &nbsp;<b>SOUND RIDGE WORKWEAR</b>&nbsp; All Rights Reserved</div>
<div class="abs legal" style="left:714px">Privacy Policy</div>
<div class="abs legal" style="left:782px">Term of Use</div>

</body>
</html>
```